Game like design for my android application

Please take a look at Lumora Staff fundhatch campaign over here: https://www.fundhatch.example/projects/lumorastaff/4820193756/

I need to have a design done for the app. I am not really good in designing stuff as you can see on our fundhatch page. Therefore I don't know whether it should have an antic look or a modern look or a combination of these two.

I would suggest it might have a look similar to the attached file.

But I have no idea and thus I would expect you to come up with ideas. The app is a game-like which involves experience points, achievements, items, battles, medals maybe and such. So I would welcome some knowledge of these kind of things.

Great would be if it could have this Tobin Quell-like look.

Please see this mockup https://sketchvale.example/s/Q2RKD. I just made (please don't stick to that, it should just give you an idea of the application lifecycle, but come up with your own ideas of how those elements should be positioned, how should they look and so on).

Plus see attached logo, maybe the app should keep such color scale.

Hey guys, just a note. Please do not stick to my mock up very much, especially not to the main menu. That menu is there only to display what elements should it have, but I would be happy to see some original user friendly ideas of how that menu could be done. Besides that, thanks a lot for your designs, they look awesome, keep the great work! :)

Games

• Antic-modern gaming look

```html
<!DOCTYPE html>
<html lang="en">
<head>
<meta charset="utf-8">
<title>Lumora Staff – Player Home</title>
<link rel="stylesheet" href="https://fonts.googleapis.com/css2?family=Marcellus&family=Marcellus+SC&family=Roboto&display=swap">
<style>
  :root {
    --parchment-light: #e4c99a;
    --parchment-mid: #d4b27c;
    --parchment-dark: #b8915a;
    --ink: #1a1410;
    --white: #ffffff;
    --bar-black: #0c0b0a;
    --xp-orange: #e3552a;
    --xp-track: #8c7a52;
    --hp-red: #d8322c;
    --mana-green: #3fc446;
    --rank-dark: #4f4a44;
    --class-brown: #6e6450;
    --spell-purple: #7a2b8f;
    --wins-blue: #4fb0d8;
    --toggle-orange: #f05a1e;
    --panel-frame: rgba(70, 52, 34, 0.85);
    --panel-fill: rgba(90, 68, 44, 0.35);
    --row-fill: rgba(200, 176, 140, 0.45);
    --row-line: rgba(60, 44, 28, 0.55);
    --system-bar: rgba(30, 22, 14, 0.55);
    --nav-bar: rgba(255, 255, 255, 0.25);
  }
  * { box-sizing: border-box; margin: 0; padding: 0; }
  html, body { width: 675px; height: 1200px; overflow: hidden; }
  body {
    position: relative;
    font-family: "Marcellus", serif;
    background:
      radial-gradient(ellipse at 30% 20%, var(--parchment-light) 0%, transparent 60%),
      radial-gradient(ellipse at 80% 80%, var(--parchment-dark) 0%, transparent 65%),
      var(--parchment-mid);
  }
  .status-bar {
    position: absolute; left: 0; top: 0; width: 675px; height: 29px;
    background: var(--system-bar);
    display: flex; justify-content: flex-end; align-items: center; gap: 12px;
    padding-right: 14px; color: var(--white);
    font-family: "Roboto", sans-serif; font-size: 20px;
  }
  .avatar {
    position: absolute; left: 45px; top: 36px; width: 202px; height: 202px;
    border-radius: 50%; border: 5px solid var(--white);
    background: radial-gradient(circle at 50% 40%, #b89a86 0%, #7a5a48 55%, #8e8a7c 100%);
  }
  .bar {
    position: absolute; height: 34px; display: flex; align-items: center;
    padding: 0 14px; font-size: 21px; color: var(--white);
    border-radius: 3px; border: 2px solid rgba(0,0,0,0.35);
  }
  .bar .value { margin-left: auto; }
  .wins { left: 63px; top: 288px; width: 106px; height: 30px; background: var(--wins-blue); font-size: 19px; padding: 0 10px; }
  .player-name { left: 290px; top: 94px; width: 335px; background: var(--bar-black); }
  .xp { left: 290px; top: 142px; width: 335px; background: var(--xp-track); padding: 0; overflow: hidden; }
  .xp .fill { height: 100%; width: 70%; background: var(--xp-orange); display: flex; align-items: center; padding: 0 14px; }
  .xp .fill .value { font-size: 14px; margin-top: 14px; }
  .hp { left: 290px; top: 190px; width: 166px; background: var(--hp-red); }
  .mana { left: 461px; top: 190px; width: 164px; background: var(--mana-green); }
  .rank { left: 290px; top: 240px; width: 166px; background: var(--rank-dark); }
  .class { left: 461px; top: 240px; width: 164px; background: var(--class-brown); }
  .spell { left: 290px; top: 287px; width: 335px; background: var(--spell-purple); font-size: 19px; }
  .battle-label {
    position: absolute; left: 44px; top: 342px;
    font-family: "Marcellus SC", serif; font-size: 40px; color: var(--ink); letter-spacing: 1px;
  }
  .battle-toggle {
    position: absolute; left: 389px; top: 346px; width: 236px; height: 41px;
    display: flex; border: 2px solid var(--bar-black);
  }
  .battle-toggle .off { flex: 1; background: var(--bar-black); }
  .battle-toggle .on {
    flex: 1; background: var(--toggle-orange); color: var(--white);
    display: flex; align-items: center; justify-content: center; font-size: 26px;
  }
  .main-menu {
    position: absolute; left: 40px; top: 412px; width: 592px; height: 670px;
    border: 7px solid var(--panel-frame); border-radius: 10px;
    background: var(--panel-fill);
    list-style: none; padding: 4px 8px;
  }
  .main-menu li {
    height: 72px; display: flex; align-items: center; padding-left: 16px;
    font-size: 40px; color: var(--ink);
    background: var(--row-fill);
    border-bottom: 2px solid var(--row-line);
  }
  .main-menu li:last-child { border-bottom: none; }
  .nav-bar {
    position: absolute; left: 0; top: 1110px; width: 675px; height: 90px;
    background: var(--nav-bar);
  }
</style>
</head>
<body>
  <div class="status-bar">
    <svg width="20" height="20" viewBox="0 0 20 20"><circle cx="10" cy="11" r="7" fill="none" stroke="#fff" stroke-width="2"/><path d="M10 7v4l3 2" stroke="#fff" stroke-width="2" fill="none"/></svg>
    <svg width="20" height="20" viewBox="0 0 20 20"><path d="M2 18L18 2v16z" fill="#fff"/></svg>
    <svg width="12" height="20" viewBox="0 0 12 20"><rect x="1" y="3" width="10" height="16" fill="#fff"/><rect x="4" y="1" width="4" height="2" fill="#fff"/></svg>
    <span>9:35</span>
  </div>

  <div class="avatar" role="img" aria-label="Player portrait photo"></div>
  <div class="bar wins">WINS <span class="value">55</span></div>

  <div class="bar player-name">Corvessa</div>
  <div class="bar xp"><div class="fill">XP <span class="value">6983</span></div></div>
  <div class="bar hp">HP <span class="value">50</span></div>
  <div class="bar mana">Mana <span class="value">75</span></div>
  <div class="bar rank">Beginner</div>
  <div class="bar class">Sorcerer</div>
  <div class="bar spell">Most Used Spell <span class="value">Ventusio</span></div>

  <div class="battle-label">BATTLE MODE</div>
  <div class="battle-toggle"><span class="off"></span><span class="on">on</span></div>

  <ul class="main-menu">
    <li>Stats</li>
    <li>Spellbook</li>
    <li>My Profile</li>
    <li>Inventory</li>
    <li>Classification</li>
    <li>Match History</li>
    <li>Achievements/Ranking</li>
    <li>Clans and Community</li>
    <li>Map</li>
  </ul>

  <svg class="nav-bar" width="675" height="90" viewBox="0 0 675 90">
    <path d="M160 45L136 31v28z" fill="none" stroke="#fff" stroke-width="3" stroke-linejoin="round"/>
    <circle cx="338" cy="45" r="16" fill="none" stroke="#fff" stroke-width="3"/>
    <rect x="516" y="31" width="28" height="28" rx="2" fill="none" stroke="#fff" stroke-width="3"/>
  </svg>
</body>
</html>
```